Travertine Marketing Postcard

We have brought quality pool building materials to our customers since 2000. We want our current customers and prospects to see concisely in a post card that we have premium/select travertine coping and pavers as well in stock at great prices. We can deliver the same quality product and service to them with the travertine as we have with our ceramic swimming pool tile. We want them to know that they can call us for a quote. We want them to know that in addition to pricing that is more than competitive, we are offering special freight rates and get the product to them in two business days.
Updates

Reason: I need more time to revise and decide.

Industry/Entity Type

Building

Requirements
Must have
• The quality of the product is premium /select. There are 8 colors and the most popular sizes. Even though the product is coming from GA we are offering special freight rates and in some cases can get the product to their project quicker than the local supplier. Orders received by 2:00PM EST can be shipped same day and received in two days. Outstanding customer service.

```html
<!DOCTYPE html>
<html lang="en">
<head>
<meta charset="utf-8">
<title>Harborline Stone Supply – Travertine Postcard</title>
<link rel="stylesheet" href="https://fonts.googleapis.com/css2?family=Roboto+Condensed:wght@700&display=swap">
<style>
  :root {
    --ink: #4a87ad;
    --ink-deep: #2d5c97;
    --rule: #6a78a8;
    --sand: #e6d8c4;
    --sand-light: #f6f0e8;
    --paper: #ffffff;
  }
  html, body {
    margin: 0;
    padding: 0;
    overflow: hidden;
    background: var(--paper);
  }
  .postcard {
    position: relative;
    width: 1200px;
    height: 943px;
    overflow: hidden;
    background: var(--paper);
    font-family: "Roboto Condensed", "Arial Narrow", sans-serif;
    font-weight: 700;
    color: var(--ink);
  }
  .decor-fan {
    position: absolute;
    left: 0;
    top: 0;
  }
  .brand {
    position: absolute;
    left: 30px;
    top: 110px;
    display: flex;
    align-items: center;
    gap: 16px;
  }
  .brand-square {
    width: 56px;
    height: 56px;
    background: var(--ink-deep);
    flex: none;
  }
  .brand-name {
    font-size: 40px;
    line-height: 1.05;
    color: var(--ink-deep);
    margin: 0;
  }
  .contact {
    position: absolute;
    left: 423px;
    top: 44px;
    font-size: 36px;
    line-height: 43px;
    margin: 0;
    font-style: normal;
  }
  .contact p { margin: 0; }
  .contact .address { margin-top: 43px; }
  .stamp-box {
    position: absolute;
    left: 925px;
    top: 44px;
    width: 228px;
    height: 237px;
    border: 3px solid var(--ink);
  }
  .headline {
    position: absolute;
    left: 46px;
    top: 316px;
    margin: 0;
    font-size: 52px;
    line-height: 1;
  }
  .selling-points {
    position: absolute;
    left: 31px;
    top: 0;
    margin: 0;
    padding: 0;
    list-style: none;
    font-size: 34px;
    line-height: 44px;
  }
  .selling-points li {
    position: absolute;
    left: 0;
    white-space: nowrap;
  }
  .point-colors   { top: 402px; }
  .point-prices   { top: 474px; }
  .point-stock    { top: 595px; }
  .point-shipping { top: 666px; }
  .point-quote    { top: 738px; }
  .selling-points .accent { color: var(--ink-deep); }
  .address-lines {
    position: absolute;
    left: 625px;
    top: 0;
    width: 540px;
  }
  .address-lines span {
    position: absolute;
    left: 0;
    width: 540px;
    height: 3px;
    background: var(--rule);
  }
</style>
</head>
<body>
<main class="postcard">
  <svg class="decor-fan" width="1200" height="943" viewBox="0 0 1200 943" role="img" aria-label="Decorative sweep of crossing travertine-tone lines">
    <defs>
      <linearGradient id="sandSweep" x1="0" y1="1" x2="1" y2="0">
        <stop offset="0" stop-color="var(--sand-light)" stop-color-fallback="#f6f0e8"/>
        <stop offset="1" stop-color="#e2d3be"/>
      </linearGradient>
    </defs>
    <path d="M575 786 Q1080 700 1160 0 L1200 0 L1200 778 Z" fill="url(#sandSweep)"/>
  </svg>

  <div class="brand">
    <span class="brand-square"></span>
    <p class="brand-name">Harborline<br>Stone Supply</p>
  </div>

  <address class="contact">
    <p>Phone: 555-014-2273</p>
    <p>Email: info@harborlinestone.com</p>
    <p class="address">1420 Harbor Ridge CT.</p>
    <p>Lakeview, GA&nbsp;&nbsp;30000</p>
  </address>

  <div class="stamp-box"></div>

  <h1 class="headline">Premium quality tiles</h1>

  <ul class="selling-points">
    <li class="point-colors">8 colors in the most popular sizes</li>
    <li class="point-prices">Competitive prices<br>and special freight rates</li>
    <li class="point-stock">In-Stock</li>
    <li class="point-shipping"><span class="accent">Same day shipping</span> arriving in 2 days</li>
    <li class="point-quote">Call for a quote</li>
  </ul>

  <div class="address-lines">
    <span style="top:409px"></span>
    <span style="top:469px"></span>
    <span style="top:529px"></span>
    <span style="top:589px"></span>
    <span style="top:649px"></span>
    <span style="top:708px"></span>
    <span style="top:768px"></span>
  </div>
</main>
</body>
</html>
```